Brochure design for 3D ultrasound company

I am looking for a clean and modern and edgy brochure for my ultrasound company. We are a fairly new company specialize in 3D/4D ultrasounds.Our brochures will be placed in OB-GYN offices in high end areas around Los Angeles, so we need something that will stand out and capture a modern woman's attention. Our logo is currently in the process of being designed, so I don't have a picture to provide quite yet, however it will be our company name"Kite + Lantern" written in a special font that looks like neon lights. I will attach a few images of what our logo will be like, and some initial content that can help provide the layout we would like for the brochure. please feel free to also take a look at our website. www.kitelanternscan.example.

Target Market(s)

Upscale trendy women.

Colors
eea4c8
33a6d7
fee18a

Requirements
Should not have
• too many colors.

```html
<!DOCTYPE html>
<html lang="en">
<head>
<meta charset="utf-8">
<title>Kite + Lantern — Trifold Brochure</title>
<link href="https://fonts.googleapis.com/css2?family=Alfa+Slab+One&family=Nunito+Sans:wght@400;600;700;800&display=swap" rel="stylesheet">
<style>
  :root{
    --page:#ece9e4;
    --blue-top:#1f8cc4;
    --blue-bottom:#2b6fa6;
    --blue-light:#a6def6;
    --sun:#fddf8a;
    --peach:#f8b98c;
    --blush:#f39292;
    --pink:#eea4c8;
    --maroon:#5c1616;
    --red:#a8202a;
    --ink:#1e1e1e;
    --paper:#f6f6f6;
    --white:#ffffff;
    --slab:"Alfa Slab One", Georgia, serif;
    --sans:"Nunito Sans", Arial, sans-serif;
  }
  *{box-sizing:border-box;margin:0;padding:0}
  html,body{width:960px;height:1200px;overflow:hidden;background:var(--page)}
  body{position:relative;font-family:var(--sans);color:var(--ink)}

  .brochure{position:absolute;left:162px;width:676px;height:523px;overflow:hidden;background:var(--paper);box-shadow:0 2px 8px rgba(0,0,0,.15)}
  .brochure--blue{top:54px;--band:linear-gradient(180deg,var(--blue-top),var(--blue-bottom));--band-sub:#cfe9f7;--brand:var(--white);--call:var(--white);--call-num:var(--blue-light)}
  .brochure--sunset{top:598px;--band:linear-gradient(90deg,var(--sun),var(--peach) 55%,var(--blush));--band-sub:var(--red);--brand:var(--white);--call:var(--red);--call-num:var(--red)}

  .panel{position:absolute;top:0;height:523px;overflow:hidden}
  .panel--guide{left:0;width:221px}
  .panel--about{left:221px;width:228px}
  .panel--cover{left:449px;width:227px}

  /* guide panel */
  .guide-bg{position:absolute;inset:0;background:linear-gradient(180deg,#fafafa 0%,#eeeeee 55%,#dcdcdc 100%)}
  .guide-band{position:absolute;left:0;top:0;width:100%;height:56px;background:var(--band);clip-path:polygon(0 0,100% 0,100% 56px,0 30px)}
  .guide-title{position:absolute;left:113px;top:24px;font-family:var(--slab);font-size:9px;font-weight:400;letter-spacing:.3px;color:var(--white)}
  .term{position:absolute;left:25px;width:180px;font-size:8px;line-height:10.4px}
  .term b{font-size:13px;font-weight:800;line-height:1}
  .term--2d{top:62px}.term--3d{top:122px}.term--4d{top:172px}.term--hd{top:221px}
  .guide-photo{position:absolute;left:0;top:314px;width:100%;height:209px;background:radial-gradient(ellipse 45% 50% at 52% 52%,#c2804f 0%,#5a4a6e 55%,#9c9c9c 80%,#bdbdbd 100%)}

  /* about panel */
  .about-bg{position:absolute;inset:0;background:linear-gradient(180deg,#ececec,#dedede)}
  .city{position:absolute;left:16px;top:48px;width:195px;height:115px;border:4px solid var(--white);background:linear-gradient(180deg,#f3b184 0%,#f6c6a0 35%,#8b7a86 55%,#5f6a4c 80%,#3c4a32 100%)}
  .city-title{position:absolute;left:0;right:0;top:8px;text-align:center;font-family:var(--slab);font-size:24px;font-weight:400;color:var(--white)}
  .about-copy{position:absolute;left:17px;top:182px;width:194px;font-size:7.3px;line-height:12px;font-weight:600;text-align:justify;text-indent:42px}
  .about-name{position:absolute;left:0;right:0;top:274px;text-align:center;font-family:var(--sans);font-size:13px;font-weight:800;color:var(--ink)}
  .contact{position:absolute;left:0;top:306px;width:100%;height:217px;background:linear-gradient(180deg,var(--sun),var(--peach) 55%,var(--blush));clip-path:polygon(0 22px,50% 0,100% 22px,100% 100%,0 100%)}
  .contact-list{position:absolute;left:0;top:314px;width:100%;list-style:none;text-align:center}
  .contact-item{height:37.5px;display:flex;flex-direction:column;align-items:center;font-size:9px;font-weight:600;color:var(--maroon)}
  .contact-item svg{width:20px;height:20px;margin-bottom:2px}

  /* cover panel */
  .cover-band{position:absolute;left:0;top:0;width:100%;height:100%;background:var(--band)}
  .brand{position:absolute;left:0;right:0;top:27px;text-align:center;font-family:var(--sans);font-size:21px;font-weight:800;line-height:24px;color:var(--brand)}
  .tagline{position:absolute;left:0;right:0;top:54px;text-align:center;font-size:8.4px;font-weight:800;color:var(--band-sub)}
  .cover-photo{position:absolute;left:0;top:80px;width:100%;height:330px;background:linear-gradient(160deg,#bdbdbd 0%,#8e8e8e 40%,#d9d9d9 75%,#efefef 100%);clip-path:polygon(0 4px,100% 0,100% 322px,0 300px)}
  .cover-white{position:absolute;left:0;top:378px;width:100%;height:30px;background:var(--white);clip-path:polygon(0 0,100% 24px,100% 30px,0 6px)}
  .ring{position:absolute;left:40px;top:214px;width:152px;height:152px;border-radius:50%;background:conic-gradient(var(--sun),var(--peach) 35%,var(--pink) 50%,var(--peach) 70%,var(--sun))}
  .ring-photo{position:absolute;left:24px;top:24px;width:104px;height:104px;border-radius:50%;background:radial-gradient(circle at 50% 60%,#b07052,#7a4a38 65%,#c9d2da 100%);display:flex;align-items:center;justify-content:center;text-align:center;font-size:9.5px;line-height:12px;font-weight:600;color:var(--white)}
  .call{position:absolute;left:0;right:0;top:414px;text-align:center;font-family:var(--slab);font-size:24px;color:var(--call)}
  .call-number{position:absolute;left:0;right:0;top:446px;text-align:center;font-family:var(--slab);font-size:24px;color:var(--call-num)}
</style>
</head>
<body>

<!-- Blue edition -->
<section class="brochure brochure--blue">
  <div class="panel panel--guide">
    <div class="guide-bg" role="img" aria-label="Faded black and white photo of a pregnant belly"></div>
    <div class="guide-band"></div>
    <h2 class="guide-title">WHAT'S WHAT?</h2>
    <p class="term term--2d"><b>2D</b> is the traditional black and white photo— you know, the one that you want to get emotional about, but you don't know what you're looking at.</p>
    <p class="term term--3d"><b>3D</b> is an image of the fetus and it's features. So you can see the baby has dad's nose, and mom's lips.</p>
    <p class="term term--4d"><b>4D</b> is 3D, but with motion. You can see the baby yawn, move it's arm, or even give you a smile.</p>
    <p class="term term--hd"><b>HD</b> is also 3D, but better. Now you can see a rendering of the baby's skin making it the most realistic fetal image possible.. we are one of the few in Los Angeles that have the newest HD capable machines</p>
    <div class="guide-photo" role="img" aria-label="Hands holding a 3D ultrasound print over a pregnant belly"></div>
  </div>

  <div class="panel panel--about">
    <div class="about-bg" role="img" aria-label="Faded city street photo"></div>
    <div class="city" role="img" aria-label="Los Angeles skyline at sunset">
      <h2 class="city-title">Los Angeles</h2>
    </div>
    <p class="about-copy">Kite + Lantern is a mobile 3D ultrasound company servicing Los Angeles, and surrounding areas. We take great pride in being one of LA's first mobile Ultrasound companies and for being an all female business! Our mission is to provide an unforgettable experience for expectant mothers in the comfort of their home!</p>
    <h3 class="about-name">Kite + Lantern</h3>
    <div class="contact"></div>
    <ul class="contact-list">
      <li class="contact-item"><svg viewBox="0 0 20 20" fill="none" stroke="#5c1616" stroke-width="1.4"><circle cx="10" cy="10" r="9"/><path d="M7 5.5l1.6 2.2-1 1.2c.7 1.4 1.8 2.5 3.2 3.2l1.2-1 2.2 1.6-.8 1.6c-3.6-.4-6.6-3.4-7-7z" fill="#5c1616"/></svg>(555) 014-2290</li>
      <li class="contact-item"><svg viewBox="0 0 20 20" fill="none" stroke="#5c1616" stroke-width="1.4"><circle cx="10" cy="10" r="9"/><ellipse cx="10" cy="10" rx="4" ry="9"/><path d="M1 10h18M3 5.5h14M3 14.5h14"/></svg>www.kitelanternscan.example</li>
      <li class="contact-item"><svg viewBox="0 0 20 20" fill="none" stroke="#5c1616" stroke-width="1.4"><circle cx="10" cy="10" r="9"/><rect x="5" y="6.5" width="10" height="7"/><path d="M5 6.5l5 4 5-4"/></svg>hello@kitelanternscan.example</li>
      <li class="contact-item"><svg viewBox="0 0 20 20"><circle cx="10" cy="10" r="8.5" fill="none" stroke="#5c1616" stroke-width="2"/></svg>kite_lantern</li>
      <li class="contact-item"><svg viewBox="0 0 20 20"><rect x="2" y="2" width="16" height="16" rx="2" fill="#5c1616"/></svg>@kitelanternscan</li>
    </ul>
  </div>

  <div class="panel panel--cover">
    <div class="cover-band"></div>
    <h1 class="brand">Kite + Lantern</h1>
    <p class="tagline">A Mobile 3D/4D Ultrasound Service</p>
    <div class="cover-photo" role="img" aria-label="Black and white photo of an expectant mother holding ultrasound prints"></div>
    <div class="cover-white"></div>
    <div class="ring">
      <div class="ring-photo" role="img" aria-label="Close-up of a pregnant belly">Ultrasound<br>in the comfort<br>of your home</div>
    </div>
    <p class="call">Call Today!</p>
    <p class="call-number">555-014-2290</p>
  </div>
</section>

<!-- Sunset edition -->
<section class="brochure brochure--sunset">
  <div class="panel panel--guide">
    <div class="guide-bg" role="img" aria-label="Faded black and white photo of a pregnant belly"></div>
    <div class="guide-band"></div>
    <h2 class="guide-title">WHAT'S WHAT?</h2>
    <p class="term term--2d"><b>2D</b> is the traditional black and white photo— you know, the one that you want to get emotional about, but you don't know what you're looking at.</p>
    <p class="term term--3d"><b>3D</b> is an image of the fetus and it's features. So you can see the baby has dad's nose, and mom's lips.</p>
    <p class="term term--4d"><b>4D</b> is 3D, but with motion. You can see the baby yawn, move it's arm, or even give you a smile.</p>
    <p class="term term--hd"><b>HD</b> is also 3D, but better. Now you can see a rendering of the baby's skin making it the most realistic fetal image possible.. we are one of the few in Los Angeles that have the newest HD capable machines</p>
    <div class="guide-photo" role="img" aria-label="Hands holding a 3D ultrasound print over a pregnant belly"></div>
  </div>

  <div class="panel panel--about">
    <div class="about-bg" role="img" aria-label="Faded city street photo"></div>
    <div class="city" role="img" aria-label="Los Angeles skyline at sunset">
      <h2 class="city-title">Los Angeles</h2>
    </div>
    <p class="about-copy">Kite + Lantern is a mobile 3D ultrasound company servicing Los Angeles, and surrounding areas. We take great pride in being one of LA's first mobile Ultrasound companies and for being an all female business! Our mission is to provide an unforgettable experience for expectant mothers in the comfort of their home!</p>
    <h3 class="about-name">Kite + Lantern</h3>
    <div class="contact"></div>
    <ul class="contact-list">
      <li class="contact-item"><svg viewBox="0 0 20 20" fill="none" stroke="#5c1616" stroke-width="1.4"><circle cx="10" cy="10" r="9"/><path d="M7 5.5l1.6 2.2-1 1.2c.7 1.4 1.8 2.5 3.2 3.2l1.2-1 2.2 1.6-.8 1.6c-3.6-.4-6.6-3.4-7-7z" fill="#5c1616"/></svg>(555) 014-2290</li>
      <li class="contact-item"><svg viewBox="0 0 20 20" fill="none" stroke="#5c1616" stroke-width="1.4"><circle cx="10" cy="10" r="9"/><ellipse cx="10" cy="10" rx="4" ry="9"/><path d="M1 10h18M3 5.5h14M3 14.5h14"/></svg>www.kitelanternscan.example</li>
      <li class="contact-item"><svg viewBox="0 0 20 20" fill="none" stroke="#5c1616" stroke-width="1.4"><circle cx="10" cy="10" r="9"/><rect x="5" y="6.5" width="10" height="7"/><path d="M5 6.5l5 4 5-4"/></svg>hello@kitelanternscan.example</li>
      <li class="contact-item"><svg viewBox="0 0 20 20"><circle cx="10" cy="10" r="8.5" fill="none" stroke="#5c1616" stroke-width="2"/></svg>kite_lantern</li>
      <li class="contact-item"><svg viewBox="0 0 20 20"><rect x="2" y="2" width="16" height="16" rx="2" fill="#5c1616"/></svg>@kitelanternscan</li>
    </ul>
  </div>

  <div class="panel panel--cover">
    <div class="cover-band"></div>
    <h1 class="brand">Kite + Lantern</h1>
    <p class="tagline">A Mobile 3D/4D Ultrasound Service</p>
    <div class="cover-photo" role="img" aria-label="Black and white photo of an expectant mother holding ultrasound prints"></div>
    <div class="cover-white"></div>
    <div class="ring">
      <div class="ring-photo" role="img" aria-label="Close-up of a pregnant belly">Ultrasound<br>in the comfort<br>of your home</div>
    </div>
    <p class="call">Call Today!</p>
    <p class="call-number">555-014-2290</p>
  </div>
</section>

</body>
</html>
```